New business card design needed for Trucking/Staffing company!

I am looking for a business card design. The business name is Harbor Lane Freightworks, LLC. This company is a staffing company for commercial drivers/truck drivers. Most of our customers are trucking/supply companies. Our colors are blue/black/white/grey. The info I have on my current business cards is
-Spot for a name
-2 lines for an address
-3 lines for Office, cell, and fax
-email
-website(currently on backside of card with logo but can go anywhere)
Updates

Project Deadline Extended
Reason: Open to more designs

Target Market(s)

Trucking companies, building supply companies

Industry/Entity Type

Business

Contact Information for Business Card

Edgy but professional

Font styles to use
Other font styles liked:
• Open to suggestions

Colors
0555a3
000000
ffffff
9d9d9d

Requirements
Must have
• Must have the logo incorporated

```html
<!DOCTYPE html>
<html lang="en">
<head>
<meta charset="utf-8">
<title>Harbor Lane Freightworks — Business Card</title>
<link rel="stylesheet" href="https://fonts.googleapis.com/css2?family=Exo+2:wght@400;700;800&family=Montserrat:wght@400;600&display=swap">
<style>
  :root {
    --brand-blue: #0555a3;
    --brand-blue-deep: #1f2f8f;
    --brand-blue-mid: #2c3fa6;
    --ink: #000000;
    --charcoal: #3a3b3e;
    --paper: #ffffff;
    --grey: #9d9d9d;
    --text-grey: #6b6b6b;
    --stage: #e9eaec;
  }
  * { box-sizing: border-box; margin: 0; padding: 0; }
  html, body { width: 1200px; height: 843px; overflow: hidden; }
  body {
    background: var(--stage);
    font-family: "Montserrat", Arial, sans-serif;
    display: flex;
    align-items: center;
    justify-content: center;
    gap: 40px;
  }
  .card {
    position: relative;
    width: 540px;
    height: 309px;
    overflow: hidden;
    box-shadow: 0 6px 18px rgba(0,0,0,0.18);
  }

  /* ---------- Back side ---------- */
  .card--back {
    background: linear-gradient(100deg, var(--charcoal) 0 38%, var(--brand-blue-deep) 38% 100%);
  }
  .card--back .truck-art {
    position: absolute;
    left: 0; top: 0;
    width: 100%; height: 100%;
  }
  .card--back .back-brand {
    position: absolute;
    right: 32px;
    bottom: 58px;
    text-align: right;
    color: var(--paper);
  }
  .back-brand .brand-name {
    font-family: "Exo 2", Arial, sans-serif;
    font-weight: 800;
    font-size: 22px;
    letter-spacing: 0.5px;
    text-transform: uppercase;
    line-height: 1.1;
  }
  .back-brand .brand-web {
    margin-top: 6px;
    font-size: 14px;
    letter-spacing: 2px;
    color: #d8dcf0;
  }

  /* ---------- Front side ---------- */
  .card--front { background: var(--paper); }
  .name-band {
    position: absolute;
    left: 0; top: 18px;
    width: 330px;
    height: 50px;
    background: var(--brand-blue-mid);
    color: var(--paper);
    padding: 6px 0 0 22px;
  }
  .name-band .person-name {
    font-family: "Exo 2", Arial, sans-serif;
    font-weight: 700;
    font-size: 18px;
    line-height: 1.1;
  }
  .name-band .person-title { font-size: 11px; margin-top: 3px; }
  .band-tail {
    position: absolute;
    left: 330px; top: 18px;
    width: 60px; height: 50px;
  }
  .front-brand {
    position: absolute;
    right: 26px;
    top: 76px;
    display: flex;
    align-items: center;
    gap: 8px;
    font-family: "Exo 2", Arial, sans-serif;
    font-weight: 800;
    font-size: 17px;
    color: var(--brand-blue-mid);
    text-transform: uppercase;
  }
  .front-brand .brand-dot {
    width: 12px; height: 12px;
    background: var(--brand-blue-mid);
    border-radius: 50%;
  }
  .address {
    position: absolute;
    left: 24px;
    top: 176px;
    font-size: 12.5px;
    line-height: 1.45;
    color: var(--text-grey);
  }
  .address .website {
    color: var(--brand-blue-mid);
    letter-spacing: 2px;
    font-weight: 600;
  }
  .contact-list {
    position: absolute;
    right: 22px;
    bottom: 26px;
    list-style: none;
    text-align: right;
    font-size: 12.5px;
    color: var(--text-grey);
  }
  .contact-list li {
    display: flex;
    justify-content: flex-end;
    align-items: center;
    gap: 8px;
    line-height: 1.55;
  }
  .contact-list svg { width: 12px; height: 12px; fill: var(--brand-blue-mid); }
</style>
</head>
<body>

  <section class="card card--back" aria-label="Business card, back">
    <svg class="truck-art" viewBox="0 0 540 309" role="img" aria-label="Large stylised truck cab illustration in grey and blue">
      <defs>
        <linearGradient id="artFade" x1="0" y1="0" x2="1" y2="1">
          <stop offset="0" stop-color="#4a4c52" stop-opacity="0.6"/>
          <stop offset="1" stop-color="#3547b8" stop-opacity="0.5"/>
        </linearGradient>
      </defs>
      <rect x="0" y="0" width="540" height="309" fill="url(#artFade)"/>
    </svg>
    <div class="back-brand">
      <div class="brand-name">Harbor Lane Freightworks</div>
      <div class="brand-web">www.harborlanefreight.com</div>
    </div>
  </section>

  <section class="card card--front" aria-label="Business card, front">
    <div class="name-band">
      <div class="person-name">Daniel Reyes</div>
      <div class="person-title">CEO/Founder</div>
    </div>
    <svg class="band-tail" viewBox="0 0 60 50" aria-hidden="true">
      <polygon points="0,0 60,50 0,50" fill="#2c3fa6"/>
    </svg>

    <div class="front-brand">
      <span class="brand-dot"></span>
      <span>Harbor Lane Freightworks</span>
    </div>

    <div class="address">
      <div>412 Dockside Avenue</div>
      <div>Tacoma, Washington 98421</div>
      <div class="website">www.harborlanefreight.com</div>
    </div>

    <ul class="contact-list">
      <li>253 410 7726
        <svg viewBox="0 0 24 24" aria-label="Office"><path d="M6.6 10.8a15.1 15.1 0 0 0 6.6 6.6l2.2-2.2c.3-.3.7-.4 1-.2 1.1.4 2.3.6 3.6.6.6 0 1 .4 1 1V20c0 .6-.4 1-1 1A17 17 0 0 1 3 4c0-.6.4-1 1-1h3.5c.6 0 1 .4 1 1 0 1.3.2 2.5.6 3.6.1.3 0 .7-.2 1z"/></svg>
      </li>
      <li>253 418 3051
        <svg viewBox="0 0 24 24" aria-label="Cell"><path d="M7 1h10a2 2 0 0 1 2 2v18a2 2 0 0 1-2 2H7a2 2 0 0 1-2-2V3a2 2 0 0 1 2-2zm0 3v14h10V4zm5 15.5a1 1 0 1 0 0 2 1 1 0 0 0 0-2z"/></svg>
      </li>
      <li>253 410 7790
        <svg viewBox="0 0 24 24" aria-label="Fax"><path d="M6 2h12v5H6zM3 8h18a1 1 0 0 1 1 1v9h-4v4H6v-4H2V9a1 1 0 0 1 1-1zm5 8v4h8v-4z"/></svg>
      </li>
      <li>dreyes@harborlanefreight.com
        <svg viewBox="0 0 24 24" aria-label="Email"><path d="M2 5h20v14H2zm2 2v.5l8 5 8-5V7z"/></svg>
      </li>
    </ul>
  </section>

</body>
</html>
```